Book Cover Design Book About Commercial Real Estate Investing

I need a book cover designed for my upcoming book.
Need cover for paperback and hardcover book.

The Book is about investing in net lease commercial property.

The book title:

The Steady Yield Manual
Proven Methods For Passive Landlord Buyers
By Mara Colby

Should be minimalist, clean, authoritative, convey money, trust, & growth
I think I like the colors white red and black.
I want a front cover at this time.

Samples I like are included. - the red white and blacks are my favorites

My company is The Corlane Circle
you can learn more about Triple Net Properties at my website
www.TheCorlaneCircle.com

the symbol NNN = Triple net in commercial real estate

Target Market(s)

Affluent male conservative investors

Industry/Entity Type

Real Estate

Requirements
Nice to have
• Sports Motif - - diagrams of sports plays from playbook
• google - Diagrams of sports plays -

```html
<!DOCTYPE html>
<html lang="en">
<head>
<meta charset="utf-8">
<title>The Steady Yield Manual — Front Cover</title>
<link rel="stylesheet" href="https://fonts.googleapis.com/css2?family=Oswald:wght@500;600&family=PT+Sans+Narrow:wght@700&display=swap">
<style>
  :root {
    --page-bg: #e9e9e9;
    --cover-top: #fbfbfb;
    --cover-bottom: #ececec;
    --brand-red: #a5121a;
    --brand-red-deep: #8e0f16;
    --brand-red-soft: #b8343a;
  }
  * { margin: 0; padding: 0; box-sizing: border-box; }
  html, body {
    width: 1200px;
    height: 900px;
    overflow: hidden;
    background: var(--page-bg);
  }
  .stage {
    width: 1200px;
    height: 900px;
    display: flex;
    align-items: center;
    justify-content: center;
  }
  .cover {
    position: relative;
    width: 500px;
    height: 860px;
    background: linear-gradient(180deg, var(--cover-top) 0%, var(--cover-bottom) 100%);
    box-shadow: 0 2px 14px rgba(0, 0, 0, 0.12);
    text-align: center;
    color: var(--brand-red);
  }
  .title {
    position: absolute;
    top: 96px;
    left: 0;
    right: 0;
    font-family: "Oswald", sans-serif;
    font-weight: 500;
    text-transform: uppercase;
    line-height: 1;
  }
  .title-lead {
    display: block;
    font-size: 50px;
    letter-spacing: 0.5px;
  }
  .title-main {
    display: block;
    font-size: 128px;
    font-weight: 600;
    letter-spacing: 1px;
    margin-top: 2px;
    line-height: 1;
  }
  .subtitle {
    position: absolute;
    top: 312px;
    left: 0;
    right: 0;
    font-family: "PT Sans Narrow", sans-serif;
    font-weight: 700;
    font-size: 23px;
  }
  .play-diagram {
    position: absolute;
    top: 408px;
    left: 120px;
    width: 266px;
    height: 186px;
    background: linear-gradient(135deg, var(--brand-red-soft) 0%, var(--brand-red-deep) 100%);
  }
  .author {
    position: absolute;
    top: 738px;
    left: 0;
    right: 0;
    font-family: "Oswald", sans-serif;
    font-weight: 500;
    font-size: 38px;
    text-transform: uppercase;
    letter-spacing: 0.5px;
  }
</style>
</head>
<body>
<main class="stage">
  <section class="cover">
    <h1 class="title">
      <span class="title-lead">The Steady Yield</span>
      <span class="title-main">Manual</span>
    </h1>
    <p class="subtitle">Proven Methods For Passive Landlord Buyers</p>
    <div class="play-diagram" role="img" aria-label="Sports play diagram of red dots, black crosses and a curved route arrow"></div>
    <p class="author">Mara Colby</p>
  </section>
</main>
</body>
</html>
```